Toner cartridge manufacturer needs stunning "Green" box design

We distribute environmentally friendly, premium, high quality re-manufactured toner cartridges. As a national wholesale Distributor, we ship products everyday all over the country and have a huge variety of customers and products. Part of our product offering is a Premium Toner Cartridge and we need a new, striking and beautifully simple box design. This box should have an emphasis on being "Green" and imply environmental friendliness. This Premium Toner Cartridge offering will not have a name brand and the box should ultimately be generic. We would like to see a well laid out 4 panel box(front, back, sides, top). There should be a continual theme and design that is consistent throughout the whole box. The front of the box should have the primary design that carries over to the other sides. Eye catching graphics and a space in the lower right hand corner for a label to be wrapped around the corner. In another corner on the front, there should be text that reads "Premium Toner Cartridge". This text should not be the focus and not take up very much space. The back panel will carry the theme over that's on the front but there will need to be 4 boxes/sections for text to describe the premium toner cartridge. The sides would allow for small logo/graphics, disclaimers and the second part of the wrap label described on the lower right hand side of the front of the box. Please look at QD, Brondil, Tuvan and other OEM toner boxes to gather inspiration for our desired overall look and feel. Please refrain from using stock art/stock images that will be easily identified or frequently used.

The attached image is a design that was previously done. We would like to see creative expansions similar to this. The layout is preferred as far as the label area and text on the back panel. The circle design on this is something we dont line. Instead graphics that emphasize the environment and being "green" are preferred. Use of the design to fill in more unused are would be nice.

Hi All,

Thanks for your designs.

The color green is not necessarily desired.  Sorry for the confusion.  Many boxes we see today are green in color and that will make it difficult for us to stand out.   

• stock graphics, common images that would be easily seen in other designs(literature, packaging, advertising)

```html
<!DOCTYPE html>
<html lang="en">
<head>
<meta charset="utf-8">
<title>Premium Toner Cartridge – Box Dieline</title>
<link rel="stylesheet" href="https://fonts.googleapis.com/css2?family=Montserrat:wght@700&family=Open+Sans:wght@400;600&display=swap">
<style>
  :root {
    --canvas: #ffffff;
    --board: #221f20;
    --ink-light: #ffffff;
    --ink-dark: #1a1a1a;
    --green: #6ab445;
    --lime: #b5cf2f;
    --teal: #8cc7c0;
    --cyan: #1fa9e0;
    --yellow: #f7e11c;
    --orange: #f39a1f;
    --red: #d2262c;
    --label-border: #6ab445;
  }
  html, body {
    margin: 0;
    padding: 0;
    width: 1200px;
    height: 1000px;
    overflow: hidden;
    background: var(--canvas);
  }
  .dieline {
    display: block;
    width: 1200px;
    height: 1000px;
  }
  .board { fill: var(--board); }
  .title-line {
    font-family: "Montserrat", sans-serif;
    font-weight: 700;
    font-size: 6.4px;
    letter-spacing: 0.1px;
  }
  .title-premium { fill: var(--green); }
  .title-toner { fill: var(--lime); }
  .title-cartridge { fill: var(--teal); }
  .panel-caption {
    font-family: "Open Sans", sans-serif;
    font-weight: 600;
    font-size: 4.6px;
    fill: var(--ink-light);
  }
  .logo-dot { fill: var(--ink-light); }
  .logo-tile { fill: var(--ink-light); }
  .logo-tile-text {
    font-family: "Open Sans", sans-serif;
    font-size: 4px;
    fill: var(--ink-dark);
    text-anchor: middle;
  }
  .body-copy {
    font-family: "Open Sans", sans-serif;
    font-size: 3.3px;
    fill: var(--ink-light);
  }
  .side-copy {
    font-family: "Open Sans", sans-serif;
    font-size: 3.6px;
    fill: var(--ink-light);
  }
  .label-area {
    fill: var(--ink-light);
    stroke: var(--label-border);
    stroke-width: 1.6;
  }
  .label-text {
    font-family: "Open Sans", sans-serif;
    font-size: 4.6px;
    fill: var(--ink-dark);
    text-anchor: middle;
  }
  .band-cyan { fill: var(--cyan); }
  .band-yellow { fill: var(--yellow); }
  .band-green { fill: var(--green); }
  .band-orange { fill: var(--orange); }
  .band-red { fill: var(--red); }
</style>
</head>
<body>
<svg class="dieline" viewBox="240 485 710 592" preserveAspectRatio="xMidYMid meet" xmlns="http://www.w3.org/2000/svg">
  <defs>
    <path id="box-outline" d="M262 720 L355 720 L355 712 Q355 707 360 707 L395 707 Q400 707 400 712 L400 720 L488 720 L488 704 Q488 697 496 697 L590 697 L590 605 Q590 597 598 597 L820 597 Q828 597 828 605 L828 622 L886 622 Q893 622 896 628 L928 700 L930 720 L930 895 L905 935 L905 970 L850 970 L850 935 L828 900 L828 970 L775 970 L775 945 L760 945 L760 970 L600 970 L600 955 L590 955 L590 895 L575 930 L575 955 L500 955 L500 930 L488 900 L475 935 L475 970 L300 970 L300 935 L262 895 Z"/>
    <clipPath id="box-clip"><use href="#box-outline"/></clipPath>
    <linearGradient id="tree-tones" x1="0" y1="0" x2="1" y2="1">
      <stop offset="0" stop-color="#9ccc4a"/>
      <stop offset="0.45" stop-color="#6ab445"/>
      <stop offset="0.75" stop-color="#8cc7c0"/>
      <stop offset="1" stop-color="#e0892a"/>
    </linearGradient>
    <linearGradient id="splash-tones" x1="0" y1="0" x2="1" y2="1">
      <stop offset="0" stop-color="#d2262c"/>
      <stop offset="0.5" stop-color="#8cc7c0"/>
      <stop offset="1" stop-color="#f39a1f"/>
    </linearGradient>
  </defs>

  <!-- box board -->
  <use class="board" href="#box-outline"/>

  <!-- colour bands running around the base -->
  <g class="base-bands" clip-path="url(#box-clip)">
    <path class="band-cyan" d="M262 872 Q600 866 930 872 L930 874.5 Q600 868.5 262 874.5 Z"/>
    <path class="band-yellow" d="M262 874.5 Q600 868.5 930 874.5 L930 879 Q600 873 262 879 Z"/>
    <path class="band-green" d="M262 879 Q600 873 930 879 L930 883.5 Q600 877.5 262 883.5 Z"/>
    <path class="band-orange" d="M262 883.5 Q600 877.5 930 883.5 L930 888.5 Q600 882.5 262 888.5 Z"/>
    <path class="band-red" d="M262 888.5 Q600 882.5 930 888.5 L930 893.5 Q600 887.5 262 893.5 Z"/>
  </g>

  <!-- front panel -->
  <g class="front-panel">
    <text class="title-line title-premium" x="267" y="740">PREMIUM</text>
    <text class="title-line title-toner" x="267" y="747.5">TONER</text>
    <text class="title-line title-cartridge" x="267" y="755">CARTRIDGE</text>
    <rect role="img" aria-label="Illustration: colourful tree with a yellow trunk and leaf-shaped drops in green, red, blue, purple, orange and teal" x="266" y="772" width="110" height="100" rx="40" fill="url(#tree-tones)"/>
    <rect class="label-area" x="432" y="803" width="121" height="82"/>
    <text class="label-text" x="492.5" y="846">Label here</text>
  </g>

  <!-- left side panel -->
  <g class="side-panel side-left">
    <text class="panel-caption" x="514" y="735">Small Logos here</text>
    <circle class="logo-dot" cx="517" cy="746" r="5"/>
    <circle class="logo-dot" cx="529" cy="746" r="5"/>
    <circle class="logo-dot" cx="541" cy="746" r="5"/>
    <circle class="logo-dot" cx="553" cy="746" r="5"/>
    <circle class="logo-dot" cx="565" cy="746" r="5"/>
    <rect role="img" aria-label="Illustration: leaf-shaped drops in red, teal and orange" x="537" y="778" width="42" height="46" rx="16" fill="url(#splash-tones)"/>
  </g>

  <!-- top flap -->
  <g class="top-flap">
    <rect role="img" aria-label="Illustration: colourful tree, shown upside down, with leaf-shaped drops in green, teal, purple, red and blue" x="720" y="600" width="100" height="92" rx="36" fill="url(#tree-tones)"/>
    <g transform="rotate(180 800 707)">
      <text class="title-line title-premium" x="784" y="703">PREMIUM</text>
      <text class="title-line title-toner" x="784" y="710.5">TONER</text>
      <text class="title-line title-cartridge" x="784" y="718">CARTRIDGE</text>
    </g>
  </g>

  <!-- back panel -->
  <g class="back-panel">
    <g class="feature-column">
      <rect class="logo-tile" x="614" y="750" width="36" height="35" rx="2.5"/>
      <text class="logo-tile-text" x="632" y="769">Logo here</text>
      <text class="body-copy" x="613" y="795">
        <tspan x="613" dy="0">Remanufactured to</tspan>
        <tspan x="613" dy="4.2">strict quality</tspan>
        <tspan x="613" dy="4.2">standards for sharp,</tspan>
        <tspan x="613" dy="4.2">even prints on every</tspan>
        <tspan x="613" dy="4.2">page you print. Each</tspan>
        <tspan x="613" dy="4.2">unit is tested</tspan>
        <tspan x="613" dy="4.2">before it ships to</tspan>
        <tspan x="613" dy="4.2">your office so you</tspan>
        <tspan x="613" dy="4.2">can count on it</tspan>
        <tspan x="613" dy="4.2">from the very first</tspan>
        <tspan x="613" dy="4.2">sheet to the last.</tspan>
        <tspan x="613" dy="4.2">Premium by design.</tspan>
      </text>
    </g>
    <g class="feature-column">
      <rect class="logo-tile" x="666" y="750" width="36" height="35" rx="2.5"/>
      <text class="logo-tile-text" x="684" y="769">Logo here</text>
      <text class="body-copy" x="665" y="795">
        <tspan x="665" dy="0">Each cartridge</tspan>
        <tspan x="665" dy="4.2">reuses a recovered</tspan>
        <tspan x="665" dy="4.2">shell and keeps</tspan>
        <tspan x="665" dy="4.2">plastic waste out of</tspan>
        <tspan x="665" dy="4.2">the landfill. Less</tspan>
        <tspan x="665" dy="4.2">waste, less energy</tspan>
        <tspan x="665" dy="4.2">and fewer new parts</tspan>
        <tspan x="665" dy="4.2">mean a smaller</tspan>
        <tspan x="665" dy="4.2">footprint for every</tspan>
        <tspan x="665" dy="4.2">office that prints</tspan>
        <tspan x="665" dy="4.2">with us each day.</tspan>
        <tspan x="665" dy="4.2">Kinder to the planet.</tspan>
      </text>
    </g>
    <g class="feature-column">
      <rect class="logo-tile" x="718" y="750" width="36" height="35" rx="2.5"/>
      <text class="logo-tile-text" x="736" y="769">Logo here</text>
      <text class="body-copy" x="717" y="795">
        <tspan x="717" dy="0">Fresh toner powder</tspan>
        <tspan x="717" dy="4.2">delivers deep</tspan>
        <tspan x="717" dy="4.2">blacks, crisp lines</tspan>
        <tspan x="717" dy="4.2">and clear text from</tspan>
        <tspan x="717" dy="4.2">the first sheet to</tspan>
        <tspan x="717" dy="4.2">the last. No streaks,</tspan>
        <tspan x="717" dy="4.2">no smudges and no</tspan>
        <tspan x="717" dy="4.2">faded corners. Your</tspan>
        <tspan x="717" dy="4.2">reports, letters</tspan>
        <tspan x="717" dy="4.2">and invoices look</tspan>
        <tspan x="717" dy="4.2">sharp every time</tspan>
        <tspan x="717" dy="4.2">you hit print.</tspan>
      </text>
    </g>
    <g class="feature-column">
      <rect class="logo-tile" x="770" y="750" width="36" height="35" rx="2.5"/>
      <text class="logo-tile-text" x="788" y="769">Logo here</text>
      <text class="body-copy" x="769" y="795">
        <tspan x="769" dy="0">Fits your printer</tspan>
        <tspan x="769" dy="4.2">just like the</tspan>
        <tspan x="769" dy="4.2">original and installs</tspan>
        <tspan x="769" dy="4.2">in seconds. Remove</tspan>
        <tspan x="769" dy="4.2">the seal, slide it in</tspan>
        <tspan x="769" dy="4.2">and print. Every</tspan>
        <tspan x="769" dy="4.2">cartridge is backed</tspan>
        <tspan x="769" dy="4.2">by our full warranty</tspan>
        <tspan x="769" dy="4.2">and a friendly team</tspan>
        <tspan x="769" dy="4.2">ready to help you</tspan>
        <tspan x="769" dy="4.2">whenever you need</tspan>
        <tspan x="769" dy="4.2">a hand with setup.</tspan>
      </text>
    </g>
  </g>

  <!-- bottom flap small marks -->
  <g class="bottom-flap-marks">
    <rect class="logo-tile" x="690" y="905" width="15" height="15" rx="2"/>
    <text class="logo-tile-text" x="697.5" y="914" style="font-size:2.8px">Logo here</text>
    <circle class="logo-tile" cx="718" cy="912.5" r="8"/>
    <text class="logo-tile-text" x="718" y="914" style="font-size:2.8px">Logo here</text>
  </g>

  <!-- right side panel -->
  <g class="side-panel side-right">
    <text class="panel-caption" x="852" y="737">Small Logos here</text>
    <circle class="logo-dot" cx="851" cy="746" r="5"/>
    <circle class="logo-dot" cx="863" cy="746" r="5"/>
    <circle class="logo-dot" cx="875" cy="746" r="5"/>
    <circle class="logo-dot" cx="887" cy="746" r="5"/>
    <circle class="logo-dot" cx="899" cy="746" r="5"/>
    <text class="side-copy" x="832" y="760">
      <tspan x="832" dy="0">Keep this cartridge sealed in its bag until</tspan>
      <tspan x="832" dy="5.8">you are ready to install it. Store the box in</tspan>
      <tspan x="832" dy="5.8">a cool, dry place away from direct sunlight</tspan>
      <tspan x="832" dy="5.8">and heat. Do not expose the drum unit to light</tspan>
      <tspan x="832" dy="5.8">for long periods. Keep out of reach of small</tspan>
      <tspan x="832" dy="5.8">children and pets. If toner touches skin, wash</tspan>
      <tspan x="832" dy="5.8">it off with cold water and soap. Do not burn</tspan>
      <tspan x="832" dy="5.8">the cartridge. Return empty cartridges to us</tspan>
      <tspan x="832" dy="5.8">for free recycling so each shell can be used</tspan>
      <tspan x="832" dy="5.8">again. This product is remanufactured and is</tspan>
      <tspan x="832" dy="5.8">not made by the printer maker. Printer names</tspan>
      <tspan x="832" dy="5.8">are used only to show which models it fits.</tspan>
      <tspan x="832" dy="5.8">Print yield is based on five percent page</tspan>
      <tspan x="832" dy="5.8">coverage. Results vary with use and settings.</tspan>
      <tspan x="832" dy="5.8">Made with care for a cleaner working world.</tspan>
    </text>
  </g>
</svg>
</body>
</html>
```